Creative/innovative law firm website

A law firm website that immediately looks different from other law firm websites. We like the color scheme (dark background with warm, neutral colors) and simple, organic logos (trees, leaves, etc.) of this website: https://brambleworth.legal/

We'll be offering creative/innovative solutions to complex problems faced by state governments, industries, other law firms, and individuals. We're located in Montana (U.S.A.), and the outdoors is a huge part of our lives and identities.

We will need a home page, an "About Us" page with a separate subpage for each attorney (two attorneys), a blog or "Publications" page, a payment portal (which will integrate with Quillo), and a "Services" page.

```html
<!DOCTYPE html>
<html lang="en">
<head>
<meta charset="utf-8">
<title>About Us – Harlow &amp; Brightwater P.C.</title>
<link href="https://fonts.googleapis.com/css2?family=Cinzel:wght@400;500&family=Lato:wght@400;700&display=swap" rel="stylesheet">
<style>
:root{
  --header:#161a2c;
  --crumb:#1c2238;
  --page:#141829;
  --team:#1a1e33;
  --footer:#0b0c13;
  --gold:#e0b98f;
  --accent:#d9a66c;
  --button:#c98a4a;
  --text:#ffffff;
  --line:#2a2e40;
  --card-border:#3a3f58;
}
*{margin:0;padding:0;box-sizing:border-box}
html,body{width:874px;height:1200px;overflow:hidden}
body{position:relative;background:var(--page);color:var(--text);font-family:'Lato',sans-serif}
.abs{position:absolute}
.serif{font-family:'Cinzel',serif}

.site-header{left:0;top:0;width:874px;height:72px;background:var(--header)}
.brand{left:117px;top:26px;font-size:14.5px;letter-spacing:.3px;white-space:nowrap}
.brand .gold{color:var(--gold)}
.nav{top:30px;font-size:10.5px;white-space:nowrap}
.nav.active{color:var(--accent)}
.caret{display:inline-block;width:0;height:0;border-left:2.5px solid transparent;border-right:2.5px solid transparent;border-top:3px solid #fff;margin-left:4px;vertical-align:middle}
.pay-btn{left:642px;top:22px;width:115px;height:27px;background:var(--button);font-family:'Cinzel',serif;font-size:9.5px;line-height:27px;text-align:center;letter-spacing:.5px}

.breadcrumb{left:0;top:72px;width:874px;height:27px;background:var(--crumb);font-size:10.5px;line-height:27px;padding-left:119px}
.breadcrumb .current{color:var(--accent)}

.section-title{left:0;width:874px;text-align:center;font-family:'Cinzel',serif;font-size:27px;display:flex;justify-content:center;align-items:center;gap:10px}
.section-title .rule{display:inline-block;width:41px;height:1px;background:var(--gold)}
.section-title .gold{color:var(--gold)}

.about-copy{left:118px;top:204px;width:272px;font-size:10.1px;line-height:18.6px}
.about-photo{left:429px;top:207px;width:327px;height:218px;border-radius:3px;background:linear-gradient(135deg,#d9dde2 0%,#a9b0b9 45%,#3b4150 75%,#7a6a55 100%)}
.about-wide{left:118px;top:434px;width:640px;font-size:10.1px;line-height:18.6px}

.team-band{left:0;top:585px;width:874px;height:438px;background:var(--team)}
.card{top:722px;width:151px;height:235px;border:1px solid var(--card-border);border-radius:4px;overflow:hidden;text-align:center}
.card .photo{width:100%;height:174px}
.card .name{margin-top:14px;font-size:10.5px}
.card .role{margin-top:8px;font-size:9.5px}
.social-overlay{left:146px;top:797px;display:flex;gap:11px}
.ring{width:23px;height:23px;border-radius:50%;border:1px solid #fff}
.ring.on{background:#fff}

.site-footer{left:0;top:1023px;width:874px;height:177px;background:var(--footer)}
.footer-brand{left:117px;top:1050px;font-size:21.5px;line-height:27px;letter-spacing:.5px}
.footer-brand .gold{color:var(--gold);padding-left:35px}
.fnav{top:1070px;font-size:10.5px;white-space:nowrap}
.fnav.active{color:var(--accent)}
.footer-rule{left:117px;top:1128px;width:640px;height:1px;background:var(--line)}
.copyright{left:116px;top:1158px;font-size:10.5px}
.copyright .gold{color:var(--accent)}
.foot-social{left:680px;top:1154px;display:flex;gap:5px}
.foot-social .ring{width:22px;height:22px;border-color:var(--gold)}
.foot-social .ring.on{background:#fff;border-color:#fff}
</style>
</head>
<body>

<header class="abs site-header"></header>
<div class="abs brand serif"><span class="gold">Harlow &amp;</span> Brightwater P.C.</div>
<div class="abs nav" style="left:356px">Home</div>
<div class="abs nav active" style="left:402px">About</div>
<div class="abs nav" style="left:449px">Our Attorneys<span class="caret"></span></div>
<div class="abs nav" style="left:543px">Services</div>
<div class="abs nav" style="left:600px">Blog</div>
<div class="abs pay-btn">Make Payment &nbsp;&gt;&gt;</div>

<nav class="abs breadcrumb">Home &nbsp;»&nbsp; <span class="current">About Us</span></nav>

<h1 class="abs section-title" style="top:158px"><span class="rule"></span><span>About <span class="gold">Us</span></span><span class="rule"></span></h1>

<p class="abs about-copy">Sed ut perspiciatis unde omnis iste natus error sit voluptatem accusantium doloremque laudantium, totam rem aperiam, eaque ipsa quae ab illo inventore veritatis et quasi architecto beatae vitae dicta sunt explicabo. Nemo enim ipsam voluptatem quia voluptas sit aspernatur aut odit aut fugit, sed quia consequuntur magni dolores eos qui ratione voluptatem sequi nesciunt. Neque porro quisquam est, qui dolorem ipsum quia dolor sit amet, consectetur, adipisci velit, sed quia non numquam eius modi tempora incidunt ut labore et dolore magnam aliquam quaerat voluptatem. Ut enim ad minima veniam, quis nostrum exercitationem ullam corporis suscipit.</p>
<div class="abs about-photo" role="img" aria-label="Three attorneys reviewing work on a laptop in a bright office"></div>
<p class="abs about-wide">Sed ut perspiciatis unde omnis iste natus error sit voluptatem accusantium doloremque laudantium, totam rem aperiam, eaque ipsa quae ab illo inventore veritatis et quasi architecto beatae vitae dicta sunt explicabo. Nemo enim ipsam voluptatem quia voluptas sit aspernatur aut odit aut fugit, sed quia consequuntur magni dolores eos qui ratione voluptatem sequi nesciunt. Neque porro quisquam est, qui dolorem ipsum quia dolor sit amet, consectetur, adipisci velit, sed quia non numquam eius modi tempora incidunt ut labore et dolore magnam aliquam quaerat voluptatem. Ut enim ad minima veniam, quis nostrum exercitationem ullam corporis suscipit.</p>

<section class="abs team-band"></section>
<h2 class="abs section-title" style="top:646px"><span class="rule"></span><span>Our <span class="gold">Team</span></span><span class="rule"></span></h2>

<div class="abs card" style="left:117px"><div class="photo" role="img" aria-label="Portrait of a team member in a navy blazer" style="background:linear-gradient(180deg,#4a5270,#2a3150)"></div><div class="name">Lorem Ipsum Dolar</div><div class="role">( Designation Here )</div></div>
<div class="abs card" style="left:277px"><div class="photo" role="img" aria-label="Portrait of a team member holding a folder" style="background:linear-gradient(180deg,#d8d4cf,#6a5a55 70%,#2a2628)"></div><div class="name">Lorem Ipsum Dolar</div><div class="role">( Designation Here )</div></div>
<div class="abs card" style="left:441px"><div class="photo" role="img" aria-label="Portrait of a team member in a dark suit" style="background:linear-gradient(180deg,#ecd3cb,#6c7260 70%,#3a4256)"></div><div class="name">Lorem Ipsum Dolar</div><div class="role">( Designation Here )</div></div>
<div class="abs card" style="left:606px"><div class="photo" role="img" aria-label="Portrait of a team member in a grey sweater" style="background:linear-gradient(180deg,#2e3f48,#8d8f92 65%,#a3a5a8)"></div><div class="name">Lorem Ipsum Dolar</div><div class="role">( Designation Here )</div></div>
<div class="abs social-overlay"><span class="ring on"></span><span class="ring"></span><span class="ring"></span></div>

<footer class="abs site-footer"></footer>
<div class="abs footer-brand serif"><div class="gold">Harlow &amp;</div><div>Brightwater P.C.</div></div>
<div class="abs fnav" style="left:411px">Home</div>
<div class="abs fnav active" style="left:476px">About</div>
<div class="abs fnav" style="left:541px">Our Attorneys<span class="caret"></span></div>
<div class="abs fnav" style="left:654px">Services</div>
<div class="abs fnav" style="left:728px">Blog</div>
<div class="abs footer-rule"></div>
<div class="abs copyright">Copyright 2021 <span class="gold">Harlow &amp; Brightwater P.C.</span> All Rights Reserved.</div>
<div class="abs foot-social"><span class="ring on"></span><span class="ring"></span><span class="ring"></span></div>

</body>
</html>
```